Business Card design for a skin clinic

i would like a business card design for our skin clinic.
our logo colors are Blue and Grey and Bule /white.
we are searching for a minimalistic design yet very elegant,dynamic and professional which can reflect a professional medical skin care clinic( not a beauty salon).
THE DESGIN IS NOT FOR A PERSON IT WILL BE USED IN THE CLINIC FOR CLIENTS SO THERE SHOULD BE NO NAME OF A PERSON ONLY THE CLINIC NAME AND THE CONTACT INFO

Target Market(s)
young and old womens
Industry/Entity Type
Business
Contact Information for Business Card
we have 2 address and both should be on the card.
address A: Lindenhoflaan 214B, 3041KP Rotterdam, Tel 010 483 21 95
address B: Zonnewijzerstraat 238, 1062RT Amsterdam Tel 020 571 3829
website www.huidpuntzorg.nu, email info@huidpuntzorg.nu
Look and feel
Each slider illustrates characteristics of the customer's brand and the style your logo design should communicate.

```html
<!DOCTYPE html>
<html lang="nl">
<head>
<meta charset="utf-8">
<title>Huidpuntzorg – visitekaartjes</title>
<link rel="stylesheet" href="https://fonts.googleapis.com/css2?family=Montserrat:wght@400;500&family=Roboto:wght@400;500&display=swap">
<style>
  :root {
    --backdrop: #e6e7e9;
    --card-dark-1: #3a3f47;
    --card-dark-2: #15181d;
    --clinic-blue: #2f7fd0;
    --clinic-blue-deep: #1a4f94;
    --clinic-blue-light: #5aa6ec;
    --swoosh: #f2f4f6;
    --swoosh-grey: #9aa1aa;
    --text-light: #ffffff;
    --text-soft: #cfd4da;
  }
  * { box-sizing: border-box; margin: 0; padding: 0; }
  html, body { width: 1200px; height: 852px; overflow: hidden; }
  body { background: var(--backdrop); position: relative; font-family: "Roboto", sans-serif; }

  .business-card {
    position: absolute;
    width: 600px;
    height: 350px;
    border-radius: 18px;
    overflow: hidden;
    box-shadow: 0 10px 24px rgba(0,0,0,0.22);
  }
  .business-card--amsterdam { left: 70px; top: 60px; }
  .business-card--rotterdam { left: 530px; top: 440px; }

  .card-art { position: absolute; inset: 0; width: 100%; height: 100%; display: block; }

  .brand {
    position: absolute;
    left: 40px;
    top: 140px;
    display: flex;
    flex-direction: column;
    gap: 8px;
  }
  .brand-name {
    display: flex;
    align-items: center;
    gap: 12px;
    font-family: "Montserrat", sans-serif;
    font-weight: 500;
    font-size: 29px;
    letter-spacing: 2px;
    color: var(--text-light);
    white-space: nowrap;
  }
  .brand-dot {
    width: 13px; height: 13px; border-radius: 50%;
    background: var(--clinic-blue);
    flex: none;
  }
  .brand-tagline {
    font-family: "Montserrat", sans-serif;
    font-weight: 400;
    font-size: 13px;
    letter-spacing: 2px;
    color: var(--text-soft);
    padding-left: 25px;
    white-space: nowrap;
  }

  .address {
    position: absolute;
    right: 30px;
    top: 24px;
    text-align: right;
    font-size: 15px;
    line-height: 1.35;
    color: var(--text-light);
  }

  .contact-list {
    position: absolute;
    right: 26px;
    top: 182px;
    list-style: none;
    text-align: right;
    font-size: 15px;
    line-height: 1.45;
    color: var(--text-light);
  }
  .contact-list li { display: flex; justify-content: flex-end; align-items: center; gap: 8px; white-space: nowrap; }
  .contact-icon { width: 13px; height: 13px; fill: none; stroke: var(--text-light); stroke-width: 1.6; flex: none; }
</style>
</head>
<body>

<article class="business-card business-card--amsterdam">
  <svg class="card-art" viewBox="0 0 600 350" preserveAspectRatio="none">
    <defs>
      <linearGradient id="dark-a" x1="0" y1="0" x2="1" y2="1">
        <stop offset="0" stop-color="var(--card-dark-1)"/>
        <stop offset="1" stop-color="var(--card-dark-2)"/>
      </linearGradient>
      <linearGradient id="blue-a" x1="0" y1="1" x2="1" y2="0">
        <stop offset="0" stop-color="var(--clinic-blue-deep)"/>
        <stop offset="0.6" stop-color="var(--clinic-blue)"/>
        <stop offset="1" stop-color="var(--clinic-blue-light)"/>
      </linearGradient>
    </defs>
    <rect width="600" height="350" fill="url(#dark-a)"/>
    <path role="img" aria-label="Foto van het interieur van de kliniek" d="M0,320 C200,340 330,320 410,240 C470,180 520,120 600,108 L600,350 L0,350 Z" fill="url(#blue-a)"/>
    <path d="M0,305 C200,327 320,308 395,230 C455,168 510,108 600,94 L600,108 C520,120 470,180 410,240 C330,320 200,340 0,320 Z" fill="var(--card-dark-2)"/>
    <path d="M0,290 C200,316 315,295 388,218 C450,152 505,96 600,80" fill="none" stroke="var(--swoosh)" stroke-width="7"/>
    <path d="M0,300 C200,322 320,305 392,225" fill="none" stroke="var(--swoosh-grey)" stroke-width="2"/>
  </svg>
  <div class="brand">
    <div class="brand-name"><span class="brand-dot"></span>HUIDPUNTZORG</div>
    <div class="brand-tagline">next generation skin care</div>
  </div>
  <p class="address">Zonnewijzerstraat 238,<br>1062RT Amsterdam</p>
  <ul class="contact-list">
    <li>020 571 3829 <svg class="contact-icon" viewBox="0 0 14 14"><path d="M3 1.5 L5 1.5 L6 4.5 L4.6 5.6 C5.4 7.3 6.7 8.6 8.4 9.4 L9.5 8 L12.5 9 L12.5 11 C12.5 12 11.5 12.8 10.5 12.5 C6 11.5 2.5 8 1.5 3.5 C1.2 2.5 2 1.5 3 1.5 Z"/></svg></li>
    <li>www.huidpuntzorg.nu <svg class="contact-icon" viewBox="0 0 14 14"><circle cx="7" cy="7" r="5.6"/><ellipse cx="7" cy="7" rx="2.4" ry="5.6"/><path d="M1.4 7 H12.6"/></svg></li>
    <li>info@huidpuntzorg.nu <svg class="contact-icon" viewBox="0 0 14 14"><rect x="1.2" y="3" width="11.6" height="8" rx="1"/><path d="M1.2 3.5 L7 8 L12.8 3.5"/></svg></li>
  </ul>
</article>

<article class="business-card business-card--rotterdam">
  <svg class="card-art" viewBox="0 0 600 350" preserveAspectRatio="none">
    <defs>
      <linearGradient id="dark-r" x1="0" y1="0" x2="1" y2="1">
        <stop offset="0" stop-color="var(--card-dark-1)"/>
        <stop offset="1" stop-color="var(--card-dark-2)"/>
      </linearGradient>
      <linearGradient id="blue-r" x1="0" y1="1" x2="1" y2="0">
        <stop offset="0" stop-color="var(--clinic-blue-deep)"/>
        <stop offset="0.6" stop-color="var(--clinic-blue)"/>
        <stop offset="1" stop-color="var(--clinic-blue-light)"/>
      </linearGradient>
    </defs>
    <rect width="600" height="350" fill="url(#dark-r)"/>
    <path role="img" aria-label="Foto van de wachtruimte van de kliniek" d="M0,320 C200,340 330,320 410,240 C470,180 520,120 600,108 L600,350 L0,350 Z" fill="url(#blue-r)"/>
    <path d="M0,305 C200,327 320,308 395,230 C455,168 510,108 600,94 L600,108 C520,120 470,180 410,240 C330,320 200,340 0,320 Z" fill="var(--card-dark-2)"/>
    <path d="M0,290 C200,316 315,295 388,218 C450,152 505,96 600,80" fill="none" stroke="var(--swoosh)" stroke-width="7"/>
    <path d="M0,300 C200,322 320,305 392,225" fill="none" stroke="var(--swoosh-grey)" stroke-width="2"/>
  </svg>
  <div class="brand">
    <div class="brand-name"><span class="brand-dot"></span>HUIDPUNTZORG</div>
    <div class="brand-tagline">next generation skin care</div>
  </div>
  <p class="address">Lindenhoflaan 214B,<br>3041KP Rotterdam</p>
  <ul class="contact-list">
    <li>010 483 21 95 <svg class="contact-icon" viewBox="0 0 14 14"><path d="M3 1.5 L5 1.5 L6 4.5 L4.6 5.6 C5.4 7.3 6.7 8.6 8.4 9.4 L9.5 8 L12.5 9 L12.5 11 C12.5 12 11.5 12.8 10.5 12.5 C6 11.5 2.5 8 1.5 3.5 C1.2 2.5 2 1.5 3 1.5 Z"/></svg></li>
    <li>www.huidpuntzorg.nu <svg class="contact-icon" viewBox="0 0 14 14"><circle cx="7" cy="7" r="5.6"/><ellipse cx="7" cy="7" rx="2.4" ry="5.6"/><path d="M1.4 7 H12.6"/></svg></li>
    <li>info@huidpuntzorg.nu <svg class="contact-icon" viewBox="0 0 14 14"><rect x="1.2" y="3" width="11.6" height="8" rx="1"/><path d="M1.2 3.5 L7 8 L12.8 3.5"/></svg></li>
  </ul>
</article>

</body>
</html>
```